Velmo BUSINESS CARD

Design an attention-grabbing business cards. Draw inspiration from the provided logo file. Please use the same font style as in the logo.
the back side of the card is for accent/decoration.

Contact Information for Business Card

PLEASE USE PROVIDED BUSINESS CARD SAMPLE

Other font styles liked:
• LUMETTE

Colors
EB3D1F
EC4F4E
F09395
F8D3D4
FCEDEE

Requirements
Must have
• RED, BLACK COLORS, SOLID BACK COLOR
Nice to have
• MAKE IT FANCY

```html
<!DOCTYPE html>
<html lang="en">
<head>
<meta charset="utf-8">
<title>Velmo Business Card</title>
<link href="https://fonts.googleapis.com/css2?family=Orbitron:wght@600&family=Mulish:ital,wght@0,300;0,400;1,300;1,400&display=swap" rel="stylesheet">
<style>
  :root {
    --backdrop: #e4e4e2;
    --card: #060707;
    --card-back: #020303;
    --red: #d4262b;
    --text-light: #d2d2d2;
    --silver-light: #d8d8d8;
    --silver-mid: #a9a9a9;
    --silver-dark: #7a7a7a;
  }
  html, body {
    margin: 0;
    padding: 0;
    width: 1200px;
    height: 846px;
    overflow: hidden;
    background: var(--backdrop);
  }
  .canvas {
    position: relative;
    width: 1200px;
    height: 846px;
  }
  .card {
    position: absolute;
    left: 346px;
    width: 508px;
    height: 290px;
    overflow: hidden;
    box-shadow: 10px 10px 14px rgba(0,0,0,0.18);
  }
  .card-front { top: 99px; background: var(--card); }
  .card-back { top: 456px; background: var(--card-back); }

  .decoration {
    position: absolute;
    left: 302px;
    top: 0;
    width: 206px;
    height: 290px;
    background: linear-gradient(90deg, var(--silver-light) 0%, var(--silver-mid) 60%, var(--silver-dark) 100%);
    clip-path: circle(150px at 155px 140px);
  }

  .holder-name {
    position: absolute;
    left: 93px;
    top: 58px;
    margin: 0;
    font-family: 'Orbitron', sans-serif;
    font-weight: 600;
    font-size: 17px;
    line-height: 20px;
    letter-spacing: 0.5px;
    color: var(--red);
  }
  .holder-role {
    position: absolute;
    left: 93px;
    top: 78px;
    margin: 0;
    font-family: 'Mulish', sans-serif;
    font-style: italic;
    font-weight: 300;
    font-size: 12.5px;
    line-height: 16px;
    color: var(--text-light);
  }
  .contact-row {
    position: absolute;
    left: 56px;
    display: flex;
    align-items: center;
    gap: 8px;
  }
  .contact-row.phone { top: 103px; }
  .contact-row.web { top: 149px; }
  .contact-row.address { top: 194px; }
  .contact-icon {
    width: 30px;
    height: 30px;
    flex: none;
  }
  .contact-text {
    margin: 0;
    font-family: 'Mulish', sans-serif;
    font-weight: 300;
    font-size: 13.5px;
    line-height: 18px;
    color: var(--text-light);
    letter-spacing: 0.2px;
  }

  .brand {
    position: absolute;
    left: 65px;
    top: 108px;
    display: flex;
    align-items: flex-start;
    gap: 13px;
  }
  .brand-square {
    width: 75px;
    height: 75px;
    background: var(--silver-mid);
  }
  .brand-words { padding-top: 2px; }
  .brand-name {
    margin: 0;
    font-family: 'Orbitron', sans-serif;
    font-weight: 600;
    font-size: 62px;
    line-height: 54px;
    letter-spacing: 3px;
    color: var(--silver-light);
  }
  .brand-tagline {
    margin: 3px 0 0 1px;
    font-family: 'Mulish', sans-serif;
    font-style: italic;
    font-weight: 300;
    font-size: 13.5px;
    line-height: 16px;
    color: var(--silver-light);
  }
</style>
</head>
<body>
<div class="canvas">

  <section class="card card-front">
    <div class="decoration" role="img" aria-label="Large silver brand emblem decoration"></div>

    <h1 class="holder-name">OWEN CASTELL</h1>
    <p class="holder-role">President</p>

    <div class="contact-row phone">
      <svg class="contact-icon" viewBox="0 0 30 30" aria-hidden="true">
        <circle cx="15" cy="15" r="15" fill="var(--red)"/>
        <path d="M11 8c1-.6 2-.3 2.4.6l1 2.4c.3.7 0 1.4-.6 1.8l-.8.5c.6 1.8 1.6 3.3 3 4.6l.8-.4c.7-.3 1.4-.1 1.8.5l1.3 2c.5.8.2 1.7-.6 2.1l-1 .5c-1.2.6-2.7.3-3.6-.6-2.8-2.6-4.4-6-4.8-9.8-.1-1.3.2-2.6 1.1-3.2z" fill="var(--text-light)"/>
      </svg>
      <p class="contact-text">Office: +555-240-1186<br>Cell: +555-240-7390</p>
    </div>

    <div class="contact-row web">
      <svg class="contact-icon" viewBox="0 0 30 30" aria-hidden="true">
        <circle cx="15" cy="15" r="15" fill="var(--red)"/>
        <path d="M8 8l15 6-6 2-2 6z" fill="var(--text-light)"/>
      </svg>
      <p class="contact-text">OCastell@velmo-LLC.com<br>www.velmo-LLC.com</p>
    </div>

    <div class="contact-row address">
      <svg class="contact-icon" viewBox="0 0 30 30" aria-hidden="true">
        <circle cx="15" cy="15" r="15" fill="var(--red)"/>
        <path d="M15 7l-8 7h2v8h4v-5h4v5h4v-8h2z" fill="var(--text-light)"/>
      </svg>
      <p class="contact-text">1480 N. 250 East,<br>Maple Ridge, IN, 46000</p>
    </div>
  </section>

  <section class="card card-back">
    <div class="brand">
      <div class="brand-square" aria-hidden="true"></div>
      <div class="brand-words">
        <p class="brand-name">VELMO</p>
        <p class="brand-tagline">SHIPPING DONE RIGHT</p>
      </div>
    </div>
  </section>

</div>
</body>
</html>
```